I am a Financial Adviser specialising in Aged Care Advice. We provide financial advice and assistance to families with loved ones entering an Aged Care facility.
We need a flyer detailing the Aged Care Packages that we offer. There will be 3 main packages & then other add ons. I need an area where the client can sign off on the package/s that they choose. I have attached a sample to demonstrate the required layout, and a copy of content. I would like the flyer to have an image as per the attached sample, and to be designed in soft pastels, blues, greens.

Financial

```html
<!DOCTYPE html>
<html lang="en">
<head>
<meta charset="utf-8">
<title>Aged Care Services Flyer</title>
<link rel="stylesheet" href="https://fonts.googleapis.com/css2?family=Oswald:wght@400;500&family=Open+Sans:ital,wght@0,400;1,400&display=swap">
<style>
  :root {
    --gold: #b8912f;
    --gold-light: #f3dc7a;
    --gold-deep: #a87d1e;
    --heading-gold: #9a7420;
    --ink: #2b2b2b;
    --grey-text: #555555;
    --body-text: #3c3c3c;
    --paper: #ffffff;
    --band-dark: #222222;
    --backdrop-top: #9a9a9a;
    --backdrop-bottom: #050505;
  }
  * { margin: 0; padding: 0; box-sizing: border-box; }
  html, body { width: 1200px; height: 1200px; overflow: hidden; }
  body {
    background: linear-gradient(180deg, var(--backdrop-top) 0%, #5a5a5a 45%, var(--backdrop-bottom) 100%);
    position: relative;
    font-family: "Open Sans", Arial, sans-serif;
  }
  .flyer {
    position: absolute;
    left: 225px; top: 76px;
    width: 750px; height: 1052px;
    background: var(--paper);
    overflow: hidden;
  }
  .brand {
    position: absolute;
    left: 48px; top: 72px;
    display: flex; align-items: center; gap: 10px;
    font-family: "Oswald", Arial, sans-serif;
    font-weight: 500;
    font-size: 27px;
    color: var(--ink);
    letter-spacing: 0.5px;
  }
  .brand-dot {
    width: 16px; height: 16px; border-radius: 50%;
    background: var(--gold);
  }
  .title {
    position: absolute;
    left: 384px; top: 30px;
    font-family: "Oswald", Arial, sans-serif;
    font-weight: 400;
    white-space: nowrap;
  }
  .title-main { color: var(--gold); font-size: 50px; }
  .title-sub { color: var(--grey-text); font-size: 40px; }
  .hero { position: absolute; left: 0; top: 130px; width: 750px; height: 440px; }
  .faint-scene {
    position: absolute; left: 0; top: 600px; width: 460px; height: 420px;
    background: radial-gradient(ellipse at 55% 45%, #ececec 0%, #f6f6f6 45%, rgba(255,255,255,0) 75%);
  }
  .package { position: absolute; color: var(--body-text); }
  .package-head {
    display: flex; align-items: center; gap: 12px;
    font-family: "Oswald", Arial, sans-serif;
    font-weight: 400;
    font-size: 21px;
    color: var(--heading-gold);
    margin-left: -26px;
    height: 26px;
  }
  .checkbox {
    width: 15px; height: 15px;
    border: 1px solid #777;
    background: var(--paper);
  }
  .package-tag {
    font-size: 11.5px; font-style: italic;
    margin-top: 10px; margin-bottom: 17px;
  }
  .package-list { list-style: none; font-size: 12.6px; font-style: italic; line-height: 16.2px; }
  .package-list li::before { content: "\2022  "; }
  .essentials { left: 75px; top: 581px; }
  .advantage { left: 413px; top: 581px; }
  .platinum { left: 75px; top: 774px; }
  .couple {
    position: absolute; left: 428px; top: 762px; width: 292px; height: 290px;
    background: linear-gradient(160deg, #e9e4dc 0%, #d8c7ae 45%, #c9b79b 100%);
    border-radius: 140px 140px 0 0;
    z-index: 2;
  }
  .band-dark {
    position: absolute; left: 360px; top: 995px; width: 390px; height: 57px;
    background: var(--band-dark);
  }
  .band-gold {
    position: absolute; left: 0; top: 971px; width: 382px; height: 81px;
    background: linear-gradient(90deg, #c49a35 0%, var(--gold-light) 45%, #c69a33 80%, var(--gold-deep) 100%);
    border-top-right-radius: 120px 81px;
  }
  .website {
    position: absolute; left: 45px; top: 998px;
    font-size: 23px; color: #2e2e2e;
    letter-spacing: 0.3px;
  }
</style>
</head>
<body>
  <main class="flyer">
    <div class="brand"><span class="brand-dot"></span>Cedarline Financial</div>

    <h1 class="title"><span class="title-main">Aged Care</span> <span class="title-sub">Services</span></h1>

    <svg class="hero" viewBox="0 0 750 440">
      <defs>
        <linearGradient id="goldSweep" x1="0" x2="1" y1="0" y2="0">
          <stop offset="0" stop-color="#c89a30"/>
          <stop offset="0.5" stop-color="#f6e07c"/>
          <stop offset="1" stop-color="#b9862a"/>
        </linearGradient>
        <linearGradient id="parkTones" x1="0" x2="0" y1="0" y2="1">
          <stop offset="0" stop-color="#a7b98a"/>
          <stop offset="0.5" stop-color="#8fae5c"/>
          <stop offset="1" stop-color="#7da04a"/>
        </linearGradient>
      </defs>
      <path d="M280,20 C420,0 620,20 750,70 L750,88 C620,40 430,26 300,28 Z" fill="#1f1f1f"/>
      <path d="M300,28 C430,22 620,44 750,96 L750,150 C640,82 470,36 300,28 Z" fill="url(#goldSweep)"/>
      <path d="M0,250 C40,320 200,430 560,400 C360,440 120,420 0,330 Z" fill="#1f1f1f"/>
      <path d="M0,230 C50,300 220,400 540,396 C300,430 80,380 0,300 Z" fill="url(#goldSweep)"/>
      <path role="img" aria-label="Photo of a three-generation family sitting together on grass in a sunny park"
            d="M0,170 C70,70 250,24 420,24 C560,24 680,60 750,118 L750,300 C660,370 480,404 330,400 C170,396 50,340 0,270 Z"
            fill="url(#parkTones)"/>
    </svg>

    <div class="faint-scene" role="img" aria-label="Faint background photo of an embracing couple"></div>

    <section class="package essentials">
      <h2 class="package-head"><span class="checkbox"></span>ESSENTIALS PACKAGE $770</h2>
      <p class="package-tag">.......When you know what you want....</p>
      <ul class="package-list">
        <li>Explanation of Aged Care Fees and Charges.</li>
        <li>Preliminary Home/Assets Assessment.*</li>
        <li>Estimated Means Tested Fee Calculation.*</li>
        <li>Preliminary Aged Care Costs.*</li>
        <li>Estimated Cash Flow Scenario.*</li>
      </ul>
    </section>

    <section class="package advantage">
      <h2 class="package-head"><span class="checkbox"></span>ADVANTAGE PACKAGE $2,970</h2>
      <p class="package-tag">....When you need to know all the options....</p>
      <ul class="package-list">
        <li>Analyse and Strategize Aged Care costs.</li>
        <li>Compare up to 5 Strategy options.</li>
        <li>Minimise Aged Care Costs (where possible).</li>
        <li>Maximise Age Pension Income (where possible).</li>
        <li>Prepare a Full Statement of Advice (SOA).</li>
        <li>Implementation of Aged Care Strategy.</li>
      </ul>
    </section>

    <section class="package platinum">
      <h2 class="package-head"><span class="checkbox"></span>PLATINUM PACKAGE $5,940</h2>
      <p class="package-tag">....When you need someone to take charge....</p>
      <ul class="package-list">
        <li>Liase with the Aged Care Facility Convenience</li>
        <li>Pension Office Nominee.</li>
        <li>Post Entry Review.</li>
        <li>Post Implementation SOA (if required).</li>
        <li>Annual Review.</li>
      </ul>
    </section>

    <div class="band-dark"></div>
    <div class="band-gold"></div>
    <p class="website">www.yourwebsite.com</p>

    <div class="couple" role="img" aria-label="Photo of a smiling senior couple embracing"></div>
  </main>
</body>
</html>
```